Stationary for Beauty and Spa School

Create a business card, letterhead and envelopes (primarily #10 envelope with and without window and catalog envelope) for a beauty and wellness school in Miami, Fl. We offer 8 different programs of study and need an eye catching look. Looking for a combination of modern yet sophisticated. Nothing corporate or business looking. Would like to have a look and feel that is similar (or incorporates aspects) of a new website we will be launching in the next 30 days (screen shot attached.)

The final design should communicate style and elegance in a down to earth and friendly way. We strive to provide our students with quality education, friendly and amicable staff and experienced instructors.
Updates

Hello. FYI, in order to print an aesthetically appealing business card, we would like to print them (the business cards) using silk printing method, with spot UV coating (on some elements, maybe the logo, or depending on the design) and die cuts. Please think of this when preparing your design.

Only 1 day left, please submit your designs for selection. Thanks

Target Market(s)

Adults 18-49 years who are mostly interested in beauty and fashion. Need a youthful & modern look, yet sophisticated and elegant.

Industry/Entity Type

School

Colors
e34197
6b449b
add136
f79021

Requirements
Must have
• Similar look and feel as website (see attached screen shot)
Same look and feel of website (see attached screenshot)
Logo
Address: 5216 SW 3rd Avenue. Miami, Fl 33155
Telephone: 305-514-9382
Fax: 786-420-5163
website/url: www.luminora.edu
incorporate Photo of blonde model (attached)
Nice to have
• Tag line: "Beautify your future." Also, maybe two-sided business card. Would be nice if we could mention our programs (maybe in the back of the card). Below are the program offerings (names cannot be changed but order is irrelevant)... Cosmetology, Barber, Spa Therapy, Massage Therapy, Makeup Artistry, Skin Care, Manicure, Pedicure & Nail Extensions, Full Specialist.

A design with text plus a beautiful photo of a model is appealing. Attached to the files is a sample of a cover for a student handbook we have created. You should use the photo of the blonde model (attached) in your design. The original (quality) version of this stock photograph has been uploaded.

Also would be nice to request clients to follow us on facebook and instagram by including the icons.
Should not have
• A corporate or business look. We are a vocational school teaching beauty and spa programs and we like our advertising to have a look that resembles the industry. We do not want a very serious look or snobby feel.

```html
<!DOCTYPE html>
<html lang="en">
<head>
<meta charset="utf-8">
<title>Luminora School of Beauty – Business Cards</title>
<link rel="stylesheet" href="https://fonts.googleapis.com/css2?family=Open+Sans:wght@400;600;700&family=Kaushan+Script&display=swap">
<style>
  :root {
    --page-bg: #ecebe8;
    --card-bg: #ffffff;
    --ink: #1d1d1d;
    --navy: #17497a;
    --program-blue: #1f5a8e;
    --text-grey: #4a4a4a;
    --rule-grey: #c9c9c9;
  }
  * { margin: 0; padding: 0; box-sizing: border-box; }
  html, body { width: 1200px; height: 720px; overflow: hidden; }
  body {
    background: var(--page-bg);
    font-family: "Open Sans", Arial, sans-serif;
    color: var(--ink);
    position: relative;
  }
  .card {
    position: absolute;
    width: 540px;
    height: 308px;
    background: var(--card-bg);
    box-shadow: 0 6px 18px rgba(0,0,0,0.18);
    overflow: hidden;
  }
  .card--front { left: 50px; top: 80px; }
  .card--back { left: 610px; top: 332px; }

  /* Front */
  .wave { position: absolute; inset: 0; width: 100%; height: 100%; }
  .front-brand { position: absolute; left: 36px; top: 112px; width: 240px; text-align: center; }
  .brand-name {
    font-weight: 700;
    font-size: 46px;
    line-height: 1;
    color: var(--ink);
    letter-spacing: 0.5px;
  }
  .brand-sub {
    font-weight: 700;
    font-size: 13px;
    color: var(--ink);
    letter-spacing: 0.6px;
    margin-top: 8px;
  }
  .divider {
    position: absolute;
    left: 292px; top: 16px;
    width: 1px; height: 132px;
    background: var(--rule-grey);
  }
  .contact {
    position: absolute;
    left: 308px; top: 18px;
    list-style: none;
    font-size: 12px;
    color: var(--text-grey);
    line-height: 1;
  }
  .contact li { display: flex; align-items: center; gap: 7px; height: 17px; }
  .contact .icon { width: 11px; height: 11px; flex: none; }
  .contact .social-mark { width: 10px; height: 10px; background: var(--text-grey); border-radius: 2px; flex: none; margin: 0 1px; }
  .contact .address { display: block; height: auto; margin-top: 8px; line-height: 1.3; }
  .tagline {
    position: absolute;
    left: 170px; bottom: 26px;
    font-family: "Kaushan Script", cursive;
    font-size: 20px;
    color: #ffffff;
    letter-spacing: 1.5px;
    transform: rotate(-9deg);
    transform-origin: left bottom;
  }

  /* Back */
  .back-brand { position: absolute; left: 0; right: 0; top: 36px; text-align: center; }
  .back-brand .brand-name { font-size: 64px; }
  .back-brand .brand-sub { font-size: 16px; margin: 6px 0 0 120px; }
  .programs { position: absolute; left: 0; right: 0; top: 168px; text-align: center; }
  .programs-title { font-size: 19px; font-weight: 600; color: var(--program-blue); margin-bottom: 8px; }
  .programs-list { list-style: none; font-size: 14px; color: var(--text-grey); line-height: 1.55; }
</style>
</head>
<body>

<section class="card card--front" aria-label="Business card front">
  <svg class="wave" viewBox="0 0 540 308" preserveAspectRatio="none" aria-hidden="true">
    <path d="M0 238 C150 300 330 190 540 142 L540 308 L0 308 Z" fill="var(--navy)"/>
    <path d="M0 226 C150 290 320 176 540 128 C330 186 150 280 0 238 Z" fill="#111"/>
  </svg>

  <div class="front-brand">
    <div class="brand-name">Luminora</div>
    <div class="brand-sub">SCHOOL OF BEAUTY</div>
  </div>

  <div class="divider"></div>

  <ul class="contact">
    <li>
      <svg class="icon" viewBox="0 0 12 12" aria-hidden="true"><circle cx="6" cy="6" r="5.3" fill="none" stroke="currentColor" stroke-width="1.2"/><path d="M4 3.5 L5 5 L4.6 5.6 Q5.4 7 6.6 7.5 L7.2 7 L8.6 8 L8 8.8 Q5 8.6 3.4 4.2 Z" fill="currentColor"/></svg>
      305-514-9382
    </li>
    <li>
      <svg class="icon" viewBox="0 0 12 12" aria-hidden="true"><path d="M2 1 H10 V11 H2 Z" fill="currentColor"/><rect x="3.3" y="2.3" width="5.4" height="6" fill="#fff"/></svg>
      786-420-5163
    </li>
    <li>
      <svg class="icon" viewBox="0 0 12 12" aria-hidden="true"><circle cx="6" cy="6" r="5.2" fill="none" stroke="currentColor" stroke-width="1.1"/><ellipse cx="6" cy="6" rx="2.2" ry="5.2" fill="none" stroke="currentColor" stroke-width="1"/><path d="M1 6 H11" stroke="currentColor" stroke-width="1"/></svg>
      www.luminora.edu
    </li>
    <li><span class="social-mark"></span>/luminorastyle</li>
    <li><span class="social-mark"></span>/luminoraedu</li>
    <li class="address">5216 SW 3rd Avenue.<br>Miami, Fl 33155</li>
  </ul>

  <div class="tagline">Beautify Your Future</div>
</section>

<section class="card card--back" aria-label="Business card back">
  <div class="back-brand">
    <div class="brand-name">Luminora</div>
    <div class="brand-sub">SCHOOL OF BEAUTY</div>
  </div>
  <div class="programs">
    <h2 class="programs-title">Program we Offer</h2>
    <ul class="programs-list">
      <li>• Cosmetology • Barber • Spa Therapy • Massage Therapy</li>
      <li>• Makeup Artistry • Skin Care • Manicure</li>
      <li>• Pedicure &amp; Nail Extensions • Full Specialist</li>
    </ul>
  </div>
</section>

</body>
</html>
```